Word Page Templates x 5

1 x Letterhead Template with Header and Footer able to be printed to paper and pdf with non blurry resolution
- File attached looks ok on computer screen but does not print the same
- We are wanting it to print like it looks on the screen
- We are wanting it to print not fuzzy in resolution
- We are wanting the banner to be on the absolute edge of the page like it is on the computer screen
- We are needing to print this to paper and pdf with perfect resolution and colour

Please can someone help us!!

I have provided the logo files in our posession. If better resolutions are required please let us know.

We are also wanting 4 simple page templates to be setup in Landscape and Portrait orientation as well once we are happy with the letterhead that is provided samples have been provided
Updates

Hi all I have the vector files available now along with a Colour profile

Requirements
Must have
• Clear when printed on A4 Paper
Should not have
• Blurry images, Colour must be correct (same as Logo) - Please reference our website if need be ..... vornal.com.au

```html
<!DOCTYPE html>
<html lang="en">
<head>
<meta charset="utf-8">
<title>Vornal Pavement Services – Letterhead (Landscape)</title>
<link href="https://fonts.googleapis.com/css2?family=Barlow:wght@600;800&display=swap" rel="stylesheet">
<style>
  :root {
    --brand-green: #0a7f44;
    --brand-teal: #176063;
    --brand-navy: #243f7f;
    --tagline-grey: #8e8e8e;
    --page-white: #ffffff;
    --canvas-bg: #ffffff;
  }
  * { margin: 0; padding: 0; box-sizing: border-box; }
  html, body {
    width: 1200px;
    height: 848px;
    overflow: hidden;
    background: var(--canvas-bg);
  }
  .letterhead {
    position: absolute;
    left: 11.5px;
    top: 7.8px;
    width: 1177px;
    height: 832px;
    background: var(--page-white);
    box-shadow: 0 0 4px rgba(0, 0, 0, 0.45);
    overflow: hidden;
  }
  .header-band {
    position: absolute;
    left: 0;
    top: 14px;
    width: 100%;
    height: 11.5px;
    background: linear-gradient(90deg, var(--brand-green), var(--brand-teal) 50%, var(--brand-navy));
  }
  .corner-accent {
    position: absolute;
    right: 0;
    bottom: 0;
    width: 66px;
    height: 208px;
    background: linear-gradient(180deg, var(--brand-navy), var(--brand-teal) 55%, var(--brand-green));
  }
  .brand {
    position: absolute;
    right: 84px;
    top: 720px;
    text-align: right;
    font-family: "Barlow", Arial, sans-serif;
  }
  .brand__name {
    display: block;
    font-weight: 800;
    font-size: 61px;
    line-height: 61px;
    letter-spacing: 1px;
    color: var(--brand-navy);
  }
  .brand__tagline {
    display: block;
    margin-top: 2px;
    font-weight: 600;
    font-size: 14.5px;
    letter-spacing: 1.2px;
    color: var(--tagline-grey);
  }
</style>
</head>
<body>
  <div class="letterhead">
    <div class="header-band"></div>
    <div class="corner-accent" role="img" aria-label="Decorative brand graphic in green, teal and navy"></div>
    <div class="brand">
      <span class="brand__name">VORNAL</span>
      <span class="brand__tagline">PAVEMENT SERVICES</span>
    </div>
  </div>
</body>
</html>
```